Brand Business Card for Hotel Cloud Management System

Hello designers,
we are looking for a new brand business card for our product Stayvora. Our brand Stayvora is a hotel management system for small hotels, B&B, guesthouses etc. and just recently we are expanding our offer to other European markets. Therefore we need a business card that will communicate not only to the end-users (hoteliers) but also to potential business partners/ We would like the brand business card to be professional looking, but not too serius, modern, elegant, clean, Our brand color is orange, dark grey and it would be nice to see both combined.

Please visit our website www.stayvora.eu to get more impression on what our brand stayvora stands for.

Please find attached stayvora logo.

Target Market(s)

small hotels, hoteliers, B&B owners, potential business partners

Industry/Entity Type

Software Service

Contact Information for Business Card

Stayvora
- hotel software solutions - web booking engine - multi channel manager
www.stayvora.eu
T: +38614738265
E: info@stayvora.net

Font styles to use
Serif
Sans Serif

Colors
f37122
aaaaaa
606060
f6f6f6

Requirements
Must have
• Logo of the brand
• the layout of the business card should be in connection with the look and feel of the website stayvora.eu and logo stayvora;

```html
<!DOCTYPE html>
<html lang="en">
<head>
<meta charset="utf-8">
<title>Stayvora business card</title>
<link rel="stylesheet" href="https://fonts.googleapis.com/css2?family=Questrial&display=swap">
<style>
  :root {
    --backdrop: #2f2f2f;
    --card-front: #f3f3f3;
    --card-back: #ffffff;
    --orange: #f37122;
    --ink: #1c1c1c;
    --grey: #606060;
  }
  * { box-sizing: border-box; margin: 0; padding: 0; }
  html, body { width: 1200px; height: 1200px; overflow: hidden; }
  body {
    background: var(--backdrop);
    font-family: "Questrial", sans-serif;
    color: var(--ink);
    position: relative;
  }
  .card {
    position: absolute;
    left: 243px;
    width: 736px;
    height: 442px;
  }
  .card--front {
    top: 112px;
    background: var(--card-front);
    display: flex;
    align-items: center;
    justify-content: center;
    gap: 18px;
  }
  .brand-dot {
    width: 34px;
    height: 34px;
    border-radius: 50%;
    background: var(--orange);
  }
  .brand-name {
    font-size: 64px;
    color: var(--orange);
    letter-spacing: 1px;
  }
  .card--back {
    top: 653px;
    background: var(--card-back);
    box-shadow: 0 8px 18px rgba(0,0,0,0.5);
  }
  .wordmark {
    position: absolute;
    top: 68px;
    left: 0;
    width: 100%;
    text-align: center;
    font-size: 84px;
    line-height: 1;
    color: var(--ink);
  }
  .taglines {
    position: absolute;
    top: 166px;
    left: 0;
    width: 100%;
    text-align: center;
    font-size: 17px;
    letter-spacing: 2.4px;
    line-height: 20px;
    color: var(--ink);
  }
  .taglines span {
    display: inline-block;
    border-bottom: 1px solid var(--ink);
    line-height: 19px;
  }
  .contacts {
    position: absolute;
    top: 263px;
    left: 214px;
    list-style: none;
  }
  .contacts li {
    display: flex;
    align-items: center;
    height: 40px;
    font-size: 20px;
    letter-spacing: 3.2px;
  }
  .contacts svg {
    width: 30px;
    height: 30px;
    margin-right: 18px;
    fill: none;
    stroke: var(--ink);
    stroke-width: 1.3;
  }
</style>
</head>
<body>
  <section class="card card--front">
    <span class="brand-dot"></span>
    <span class="brand-name">Stayvora</span>
  </section>

  <section class="card card--back">
    <h1 class="wordmark">Stayvora</h1>
    <p class="taglines">
      <span>hotel software solutions </span><br>
      <span>web booking engine - multi channel manager</span>
    </p>
    <ul class="contacts">
      <li>
        <svg viewBox="0 0 30 30" aria-hidden="true">
          <path d="M6 4 L11 4 L13 10 L10 12 Q13 19 19 21 L21 18 L27 20 L27 25 Q26 28 22 27 Q9 24 4 9 Q3 5 6 4 Z"/>
        </svg>
        +38614738265
      </li>
      <li>
        <svg viewBox="0 0 30 30" aria-hidden="true">
          <rect x="2" y="7" width="26" height="17"/>
          <path d="M2 7 L15 17 L28 7 M2 24 L12 15 M28 24 L18 15"/>
        </svg>
        info@stayvora.net
      </li>
      <li>
        <svg viewBox="0 0 30 30" aria-hidden="true">
          <circle cx="15" cy="15" r="12"/>
          <ellipse cx="15" cy="15" rx="5.5" ry="12"/>
          <path d="M3 15 H27 M15 3 V27 M5 9 H25 M5 21 H25"/>
        </svg>
        www.stayvora.eu
      </li>
    </ul>
  </section>
</body>
</html>
```